Dashboard Design For A Web App

Dashboard design. Layout and creative design ONLY. I already have developed the infrastructure.
This project is for someone to put together a creative modern design to my mock up. No coding no dev work just good old fashioned imagery.

The dashboard is for software that works out the profitability of a product.

The user will input the purchase price, sale price, quantity and pricing strategy and the software will spit out metrics confirming the profitability of the product. I have attached an image of the mock up design to give you a plan on what needs to be shown.

So the plan is to take my mock up and design a custom look that displays all the information in an eye catching easy to follow layout.

This should be a really cool job for someone who likes this type of design.

If you have designed a dashboard in the past feel free to show me I would love to see your work.

Also I really like the small details in design I think it separates the best from the good. It shows that some planning and thought has gone into it and I appreciate that in peoples work.

I will post the mock up very soon. Any questions feel free to ask :)

```html
<!DOCTYPE html>
<html lang="en">
<head>
<meta charset="utf-8">
<title>Profitly — Product Profitability Dashboard</title>
<link rel="stylesheet" href="https://fonts.googleapis.com/css2?family=Open+Sans:ital,wght@0,400;0,600;1,400&family=Nunito:wght@800;900&family=Quicksand:wght@300;400&display=swap">
<style>
:root{
  --accent:#03b9d5;
  --accent-2:#4fd3e3;
  --accent-3:#85dfeb;
  --accent-4:#a8ebf2;
  --accent-5:#69c3cf;
  --page:#f0f0f0;
  --panel:#ffffff;
  --ink:#555555;
  --ink-soft:#8a8a8a;
  --ink-faint:#a8a8a8;
  --dark:#4f4f4f;
  --green:#5cb85c;
  --red:#e04848;
  --grid:#e3e3e3;
}
*{box-sizing:border-box;margin:0;padding:0}
html,body{width:1200px;height:2335px;overflow:hidden}
body{background:var(--page);font-family:"Open Sans",Arial,sans-serif;color:var(--ink);position:relative}
.abs{position:absolute}

/* header */
.topbar{left:0;top:0;width:1200px;height:58px;background:#fff;border-bottom:1px solid #e2e2e2}
.brand{left:151px;top:12px;font-family:"Open Sans",Arial,sans-serif;font-weight:600;font-size:24px;color:#9a9a9a;letter-spacing:.5px}
.nav-item{top:0;height:58px;width:110px;text-align:center;font-size:11px;color:#a8a8a8;text-transform:uppercase;padding-top:6px}
.nav-item svg{display:block;margin:0 auto 4px;width:24px;height:24px}
.nav-item.is-active{background:var(--accent);color:#fff}
.login{left:963px;top:13px;width:86px;height:30px;border-radius:15px;background:#9a9a9a;color:#fff;font-size:12px;text-align:center;line-height:30px;box-shadow:0 2px 3px rgba(0,0,0,.2)}

/* selects */
.select{top:87px;height:48px;background:#fff;box-shadow:0 1px 2px rgba(0,0,0,.08);font-size:12px;color:#777;padding:0 14px;line-height:48px;text-transform:uppercase}
.select::after{content:"▾";position:absolute;right:14px;top:0;color:#bbb;font-size:14px}

/* input cards */
.input-card{top:191px;height:174px;background:#fff;box-shadow:0 1px 3px rgba(0,0,0,.08);text-align:center}
.input-card .label{position:absolute;left:0;right:0;top:58px;font-size:19px;font-weight:600;color:#888;letter-spacing:.3px}
.input-card .value{position:absolute;left:0;right:0;top:96px;font-family:"Quicksand",sans-serif;font-size:42px;color:#444}
.step{top:160px;width:72px;height:63px;background:var(--accent);color:#fff;font-family:"Quicksand",sans-serif;font-weight:300;font-size:38px;text-align:center;line-height:63px}

/* panels */
.panel{left:152px;width:897px;background:var(--panel);box-shadow:0 1px 3px rgba(0,0,0,.06)}
.panel-head{left:152px;width:897px;background:var(--accent);color:#fff;font-family:"Nunito",sans-serif;font-weight:900;font-size:22px;letter-spacing:.4px;padding-left:15px}
.strategy{top:403px;height:49px;line-height:49px;font-family:"Open Sans",sans-serif;font-weight:400;font-size:12px;letter-spacing:0}
.strategy::after{content:"▼";position:absolute;right:14px;font-size:11px}
.metric-label{top:477px;width:300px;text-align:center;font-family:"Nunito",sans-serif;font-weight:800;font-size:22px;color:#8a8a8a;letter-spacing:.3px}
.hint{right:15px;top:15px;font-family:"Open Sans",sans-serif;font-weight:600;font-size:11px;letter-spacing:0}

.axis{font-family:"Open Sans",sans-serif;font-size:12px;fill:#888}
.growth-label{left:187px;top:1330px;font-family:"Nunito",sans-serif;font-weight:800;font-size:20px;color:#666}
.spinner{top:1320px;height:48px;background:#fff;box-shadow:0 1px 3px rgba(0,0,0,.12);font-size:12px;color:#666;line-height:48px;padding-left:10px}
.spinner::after{content:"▲\A▼";white-space:pre;position:absolute;right:14px;top:12px;line-height:11px;font-size:9px;color:#aaa}

/* costs table */
.costs{left:609px;top:1837px;width:403px;height:336px;background:#f3f3f3}
.costs-head{left:0;top:0;width:403px;height:48px;background:var(--accent);color:#fff;font-family:"Nunito",sans-serif;font-weight:800;font-size:22px;text-align:center;line-height:48px;letter-spacing:.5px}
.cost-row{left:12px;width:376px;height:45px;background:#fff;border-left:6px solid var(--accent);box-shadow:0 1px 2px rgba(0,0,0,.08);font-style:italic;font-size:14px;color:#777;line-height:45px;padding:0 14px}
.cost-row span{position:absolute;right:14px}
.footer{left:0;top:2280px;width:1200px;height:55px;background:#fff;text-align:center;font-size:12px;color:#888;line-height:50px}
</style>
</head>
<body>

<header class="abs topbar">
  <div class="abs brand">PROFITLY</div>
  <div class="abs nav-item is-active" style="left:335px">
    <svg viewBox="0 0 24 24" fill="none" stroke="#fff" stroke-width="1.6"><rect x="9" y="3" width="6" height="18" rx="3"/><line x1="9" y1="9" x2="15" y2="9"/></svg>Test</div>
  <div class="abs nav-item" style="left:445px">
    <svg viewBox="0 0 24 24" fill="var(--accent)"><rect x="3" y="15" width="3" height="6"/><rect x="8" y="12" width="3" height="9"/><rect x="13" y="9" width="3" height="12"/><rect x="18" y="6" width="3" height="15"/><path d="M3 10 L10 5 L14 8 L21 2" stroke="var(--accent)" stroke-width="1.6" fill="none"/></svg>Growth</div>
  <div class="abs nav-item" style="left:572px">
    <svg viewBox="0 0 24 24"><text x="3" y="19" font-size="20" font-weight="700" fill="var(--accent)" font-family="Arial,sans-serif">$</text><circle cx="18" cy="17" r="4" fill="var(--accent)"/></svg>Costs</div>
  <div class="abs nav-item" style="left:686px">
    <svg viewBox="0 0 24 24" fill="var(--accent)"><rect x="3" y="4" width="3" height="3"/><rect x="8" y="4" width="13" height="3"/><rect x="3" y="10.5" width="3" height="3"/><rect x="8" y="10.5" width="13" height="3"/><rect x="3" y="17" width="3" height="3"/><rect x="8" y="17" width="13" height="3"/></svg>Summary</div>
  <div class="abs nav-item" style="left:802px">
    <svg viewBox="0 0 24 24" fill="var(--accent)"><circle cx="10" cy="14" r="6"/><circle cx="10" cy="14" r="2.2" fill="#fff"/><circle cx="18" cy="6" r="4"/><circle cx="18" cy="6" r="1.4" fill="#fff"/></svg>Settings</div>
  <div class="abs login">LOGIN</div>
</header>

<div class="abs select" style="left:152px;width:441px">Test Product</div>
<div class="abs select" style="left:609px;width:440px">Monthly</div>

<section class="abs input-card" style="left:152px;width:289px"><div class="label">PRODUCT COST</div><div class="value">25</div></section>
<section class="abs input-card" style="left:456px;width:289px"><div class="label">SALE PRICE</div><div class="value">50</div></section>
<section class="abs input-card" style="left:760px;width:289px"><div class="label">QUANTITY</div><div class="value">100</div></section>
<div class="abs step" style="left:169px">1</div>
<div class="abs step" style="left:474px">2</div>
<div class="abs step" style="left:778px">3</div>

<!-- strategy / metrics -->
<section class="abs panel" style="top:403px;height:425px"></section>
<div class="abs panel-head strategy">High Volume / Low Pricing Strategy</div>
<div class="abs metric-label" style="left:294px">PROFIT PER UNIT</div>
<div class="abs metric-label" style="left:610px">PROFIT MARGIN</div>
<svg class="abs" style="left:300px;top:509px" width="620" height="290" viewBox="300 509 620 290">
  <circle cx="444" cy="653" r="132" fill="#f4f4f4"/>
  <circle cx="444" cy="653" r="129" fill="#f8f8f8"/>
  <path d="M444 524 A129 129 0 0 0 444 782 Z" fill="var(--accent)"/>
  <circle cx="444" cy="653" r="69" fill="#fff"/>
  <text x="444" y="666" text-anchor="middle" font-family="Nunito,sans-serif" font-weight="900" font-size="36" fill="#555">$25</text>
  <circle cx="760" cy="653" r="132" fill="#f4f4f4"/>
  <circle cx="760" cy="653" r="129" fill="#f8f8f8"/>
  <path d="M760 524 A129 129 0 0 0 760 782 Z" fill="var(--dark)"/>
  <circle cx="760" cy="653" r="69" fill="#fff"/>
  <text x="760" y="666" text-anchor="middle" font-family="Nunito,sans-serif" font-weight="900" font-size="36" fill="#555">50%</text>
</svg>

<!-- gross profit -->
<section class="abs panel" style="top:857px;height:359px"></section>
<div class="abs panel-head" style="top:857px;height:46px;line-height:46px">GROSS PROFIT<span class="abs hint">**Drag black boxes to adjust values</span></div>
<svg class="abs" style="left:190px;top:936px" width="810" height="260" viewBox="190 936 810 260">
  <rect x="221" y="940" width="762" height="224" fill="#f5f5f5"/>
  <g stroke="#e6e6e6"><line x1="401" y1="940" x2="401" y2="1164"/><line x1="575" y1="940" x2="575" y2="1164"/><line x1="745" y1="940" x2="745" y2="1164"/><line x1="917" y1="940" x2="917" y2="1164"/></g>
  <g stroke="#9a9a9a" stroke-dasharray="1 3"><line x1="226" y1="977" x2="978" y2="977"/><line x1="226" y1="1015" x2="978" y2="1015"/><line x1="226" y1="1052" x2="978" y2="1052"/><line x1="226" y1="1089" x2="978" y2="1089"/><line x1="226" y1="1127" x2="978" y2="1127"/></g>
  <polygon points="231,1153 401,1091 575,1052 748,1091 919,1053 919,1164 231,1164" fill="#e3f4f1" opacity=".8"/>
  <polyline points="231,1153 401,1091 575,1052 748,1091 919,1053" fill="none" stroke="var(--accent)" stroke-width="1.2"/>
  <circle cx="231" cy="1153" r="4" fill="#fff" stroke="#666" stroke-width="2"/>
  <circle cx="401" cy="1091" r="4" fill="#fff" stroke="var(--red)" stroke-width="2"/>
  <circle cx="575" cy="1052" r="4" fill="#fff" stroke="var(--green)" stroke-width="2"/>
  <circle cx="748" cy="1091" r="4" fill="#fff" stroke="var(--red)" stroke-width="2"/>
  <circle cx="919" cy="1053" r="4" fill="#fff" stroke="var(--green)" stroke-width="2"/>
  <rect x="512" y="1000" width="125" height="31" fill="var(--green)"/>
  <path d="M570 1031 L575 1037 L580 1031 Z" fill="var(--green)"/>
  <text x="575" y="1020" text-anchor="middle" font-family="Open Sans,sans-serif" font-size="11" fill="#fff">GROSS PROFIT - 2,500</text>
  <g class="axis" text-anchor="end"><text x="207" y="981">$</text><text x="210" y="1019">75</text><text x="210" y="1056">50</text><text x="210" y="1093">25</text><text x="207" y="1131">0</text></g>
  <g class="axis" text-anchor="middle"><text x="225" y="1185">25</text><text x="399" y="1185">50</text><text x="575" y="1185">75</text><text x="745" y="1185">100</text><text x="917" y="1185">125</text><text x="969" y="1185">QTY</text></g>
</svg>

<!-- growth projections -->
<section class="abs panel" style="top:1248px;height:453px"></section>
<div class="abs panel-head" style="top:1248px;height:45px;line-height:45px;padding-left:12px">GROWTH PROJECTIONS</div>
<div class="abs growth-label">GROWTH</div>
<div class="abs spinner" style="left:317px;width:298px">Month</div>
<div class="abs spinner" style="left:629px;width:308px">10%</div>
<svg class="abs" style="left:260px;top:1385px" width="690" height="295" viewBox="260 1385 690 295">
  <g stroke="var(--grid)" fill="none"><rect x="313" y="1400" width="622" height="248"/>
  <line x1="437" y1="1400" x2="437" y2="1648"/><line x1="561" y1="1400" x2="561" y2="1648"/><line x1="685" y1="1400" x2="685" y2="1648"/><line x1="809" y1="1400" x2="809" y2="1648"/>
  <line x1="313" y1="1463" x2="935" y2="1463"/><line x1="313" y1="1524" x2="935" y2="1524"/><line x1="313" y1="1585" x2="935" y2="1585"/></g>
  <polygon points="313,1628 372,1608 436,1617 499,1576 561,1597 621,1571 705,1616 788,1569 887,1544 935,1555 935,1648 313,1648" fill="#e6eefb" opacity=".85"/>
  <polyline points="313,1628 372,1608 436,1617 499,1576 561,1597 621,1571 705,1616 788,1569 887,1544 935,1555" fill="none" stroke="var(--accent)" stroke-width="1.6"/>
  <g fill="#fff" stroke="var(--accent)" stroke-width="1.6"><circle cx="372" cy="1608" r="5.5"/><circle cx="436" cy="1617" r="5.5"/><circle cx="499" cy="1576" r="5.5"/><circle cx="561" cy="1597" r="5.5"/><circle cx="621" cy="1571" r="5.5"/><circle cx="705" cy="1616" r="5.5"/><circle cx="788" cy="1569" r="5.5"/><circle cx="887" cy="1544" r="5.5"/></g>
  <g class="axis" text-anchor="end"><text x="302" y="1404">8000</text><text x="302" y="1466">6000</text><text x="302" y="1528">4000</text><text x="302" y="1589">2000</text></g>
  <g class="axis" text-anchor="middle"><text x="324" y="1668">May</text><text x="449" y="1668">June</text><text x="571" y="1668">July</text><text x="696" y="1668">Aug</text><text x="823" y="1668">Sept</text></g>
</svg>

<!-- cost breakdown -->
<section class="abs panel" style="top:1743px;height:480px"></section>
<div class="abs panel-head" style="top:1743px;height:45px;line-height:45px">COST BREAK-DOWN | ADDITIONAL COST</div>
<svg class="abs" style="left:213px;top:1830px" width="340" height="340" viewBox="213 1830 340 340">
  <circle cx="383" cy="2000" r="161" fill="#f3f3f3"/>
  <circle cx="383" cy="2000" r="152" fill="#fff"/>
  <g stroke="#fff" stroke-width="3">
    <path d="M383 2000 L323.2 2134.3 A147 147 0 0 1 380.4 1853 Z" fill="var(--accent)"/>
    <path d="M383 2000 L380.4 1853 A147 147 0 0 1 493.9 1903.6 Z" fill="var(--accent-5)"/>
    <path d="M383 2000 L493.9 1903.6 A147 147 0 0 1 529.8 2007.7 Z" fill="var(--accent-3)"/>
    <path d="M383 2000 L529.8 2007.7 A147 147 0 0 1 465.2 2121.9 Z" fill="var(--accent-4)"/>
    <path d="M383 2000 L465.2 2121.9 A147 147 0 0 1 323.2 2134.3 Z" fill="var(--accent-2)"/>
  </g>
  <circle cx="383" cy="2000" r="10" fill="#fff"/>
  <g font-family="Open Sans,sans-serif" font-size="12" fill="#fff" text-anchor="middle">
    <text x="311" y="2001">Business costs</text><text x="413" y="1929">Net %</text><text x="470" y="1977">Tex %</text><text x="465" y="2046">Employees</text><text x="387" y="2090">Profit</text>
  </g>
</svg>

<section class="abs costs">
  <div class="abs costs-head">COSTS</div>
  <div class="abs cost-row" style="top:61px">BUSINESS COST<span>0000</span></div>
  <div class="abs cost-row" style="top:114px;border-left-color:var(--accent-3)">TEX<span>0000</span></div>
  <div class="abs cost-row" style="top:167px;border-left-color:var(--accent-4)">EMPLOYEE COST<span>0000</span></div>
  <div class="abs cost-row" style="top:220px;border-left-color:var(--accent-2)">PROFIT<span>0000</span></div>
  <div class="abs cost-row" style="top:273px;border-left-color:var(--accent-5)">NET PROFIT<span>0000</span></div>
</section>

<footer class="abs footer">Copyright © loremipsum 2016</footer>
</body>
</html>
```